German Webagency needs fresh modern Design

Our website is 4 years old. We need an fresh modern website. All pics we used before are from customers or handmade by us. the new website should be clear with nice handling. please dont copy something from template websites. it would be great if you can surprise us with something great. its our first project here. don´t worry if i make a mistake in responding or briefing. after 20 years you can´t see the works of your own "designer" so we hope for help :-)
our existing site: www.tovankreativ.de
Target Market(s)
small and middle sized companys in germany
Number of Pages Required
4 page
Font styles to use
Colors
Designer to choose colors to be used in the design.
Requirements
Must have
- Responsive (sure we code it)
- Modern and big Font ..Headlines and Slider
- innovative..if you know something new..feel free to show
Nice to have
- the site with our works/refences should look great and later easy to handle when we code it or use wp.
- we like black and grey but if you have better ideas also feel free
Should not have
- a cup of coffe..laptop.. a pencil a handwritten font
- dont copy and modify templates from know websites..bad style

```html
<!DOCTYPE html>
<html lang="en">
<head>
<meta charset="utf-8">
<title>Tovan Kreativ – Web Design &amp; Graphic Design</title>
<link rel="stylesheet" href="https://fonts.googleapis.com/css2?family=Poppins:wght@400;500;600;700&family=Open+Sans:wght@400;600;700&display=swap">
<style>
:root{
  --blue:#1f6cc4;
  --blue-dark:#17549e;
  --ink:#1d1d1d;
  --text:#555;
  --muted:#9a9a9a;
  --line:#e4e7ec;
  --bg-soft:#f6f8fb;
  --black:#050505;
  --white:#fff;
}
*{margin:0;padding:0;box-sizing:border-box}
html,body{width:1200px;height:4306px;overflow:hidden}
body{position:relative;background:var(--white);font-family:"Open Sans",Arial,sans-serif;color:var(--text)}
h1,h2,h3,.brand{font-family:"Poppins",Arial,sans-serif}

/* header */
.site-header{position:absolute;left:0;top:0;width:1200px;height:120px;background:var(--white);border-top:4px solid var(--blue)}
.brand{position:absolute;font-weight:700;color:var(--ink);font-size:30px;letter-spacing:-.5px;display:flex;align-items:center;gap:10px}
.brand .dot{width:14px;height:14px;border-radius:50%;background:var(--blue)}
.site-header .brand{left:100px;top:58px}
.call{position:absolute;right:100px;top:18px;display:flex;align-items:center;gap:12px;font-family:"Poppins",sans-serif;font-weight:600;font-size:17px;color:var(--ink)}
.call-icon{width:34px;height:34px;border-radius:50%;border:2px solid var(--blue);display:flex;align-items:center;justify-content:center}
.main-nav{position:absolute;right:100px;top:74px;display:flex;gap:34px;font-family:"Poppins",sans-serif;font-size:13px;font-weight:500;color:var(--ink);letter-spacing:.3px}

/* hero */
.hero{position:absolute;left:0;top:120px;width:1200px;height:680px}
.hero-photo{position:absolute;inset:0;background:radial-gradient(ellipse at 60% 45%,#e09a3a 0%,#8a4f1c 18%,#1e2a46 45%,#0b1630 75%)}
.hero h1{position:absolute;left:175px;top:262px;font-size:56px;font-weight:700;color:var(--white);letter-spacing:-1px;white-space:nowrap}
.hero-arrows{position:absolute;left:300px;top:560px;display:flex;gap:8px}
.hero-arrows span{width:34px;height:34px;border-radius:50%;border:2px solid var(--white);display:flex;align-items:center;justify-content:center}
.hero-curve{position:absolute;left:0;top:540px}

/* section headings */
.section-title{position:absolute;left:0;width:1200px;text-align:center;font-size:46px;font-weight:500;color:var(--ink)}
.section-sub{position:absolute;left:0;width:1200px;text-align:center;font-size:15px;color:var(--muted)}
.section-rule{position:absolute;left:576px;width:48px;height:3px;background:var(--blue)}

/* services */
.services-bg{position:absolute;left:0;top:800px;width:1200px;height:1085px;background:linear-gradient(180deg,#fff 0%,#f5f7fa 50%,#fff 100%)}
.service{position:absolute;width:340px}
.service-icon{width:60px;height:60px}
.service h3{font-size:23px;font-weight:500;color:var(--ink);margin:12px 0 14px}
.service p{font-size:14px;line-height:25px;color:var(--muted)}
.services-divider-v{position:absolute;left:600px;top:1080px;width:1px;height:560px;background:var(--line)}
.services-divider-h{position:absolute;left:170px;top:1362px;width:860px;height:1px;background:var(--line)}
.center-badge{position:absolute;left:540px;top:1342px;width:120px;height:40px;border-radius:20px;background:var(--white);border:1px solid var(--line);display:flex;align-items:center;justify-content:center;font-family:"Poppins",sans-serif;font-weight:700;font-size:12px;color:var(--ink)}
.btn-outline{position:absolute;display:flex;align-items:center;justify-content:center;border:1px solid #cfd8e3;border-radius:28px;font-family:"Poppins",sans-serif;font-size:14px;color:var(--blue);background:var(--white);letter-spacing:.5px}

/* about */
.about{position:absolute;left:0;top:1885px;width:1200px;height:500px}
.about-photo{position:absolute;left:560px;top:0;width:640px;height:500px;background:linear-gradient(120deg,#6e6a66 0%,#b9b2a6 40%,#d8c46a 60%,#3b3b3b 100%)}
.about-panel{position:absolute;left:0;top:0}
.about h2{position:absolute;left:100px;top:52px;font-size:42px;font-weight:600;color:var(--white)}
.about .lead{position:absolute;left:100px;top:116px;font-size:17px;color:var(--white)}
.about p.copy{position:absolute;left:100px;width:450px;font-size:14px;line-height:27px;color:#e6eefa}
.btn-white{position:absolute;left:100px;top:390px;width:132px;height:44px;border-radius:22px;background:var(--white);color:var(--blue-dark);font-family:"Poppins",sans-serif;font-size:14px;font-weight:500;display:flex;align-items:center;justify-content:center}

/* testimonials */
.clients-bg{position:absolute;left:0;top:2385px;width:1200px;height:575px;background:var(--bg-soft)}
.quote-mark{position:absolute;font-family:"Poppins",sans-serif;font-size:90px;font-weight:700;color:var(--blue);line-height:1}
.testimonial{position:absolute;width:300px;font-size:13px;line-height:28px;color:var(--muted);font-style:italic}
.testimonial .author{display:block;font-style:normal;font-weight:600;color:var(--blue-dark);margin-top:6px}
.avatar{position:absolute;width:124px;height:124px;border-radius:50%;border:5px solid var(--white);box-shadow:0 4px 14px rgba(0,0,0,.12)}
.slider-arrow{position:absolute;width:38px;height:38px;border-radius:50%;border:1px solid #bbb;background:var(--white);display:flex;align-items:center;justify-content:center}

/* blog */
.post{position:absolute;width:310px}
.post-image{width:310px;height:218px}
.post h3{font-size:18px;font-weight:500;color:var(--ink);margin-top:30px}
.post-meta{display:flex;gap:18px;font-size:13px;color:var(--text);margin-top:12px}
.post-meta span::before{content:"";display:inline-block;width:9px;height:9px;background:var(--blue);border-radius:2px;margin-right:7px}
.post p{font-size:12px;line-height:22px;color:var(--muted);margin-top:12px}
.post .btn-outline{position:relative;width:118px;height:36px;margin-top:20px;font-size:13px;color:var(--blue-dark)}

/* footer */
.site-footer{position:absolute;left:0;top:3740px;width:1200px;height:566px}
.footer-curve{position:absolute;left:0;top:0}
.footer-inner{position:absolute;left:0;top:170px;width:1200px;height:396px;background:var(--black)}
.site-footer .brand{right:100px;top:130px;color:var(--white);font-size:36px}
.site-footer .brand .dot{background:var(--white)}
.contact-title{position:absolute;left:100px;top:218px;font-size:17px;font-weight:600;color:var(--blue);letter-spacing:.5px}
.contact-item{position:absolute;font-size:12px;line-height:20px;color:#dcdcdc;padding-left:30px}
.contact-item strong{color:var(--white);font-weight:600}
.contact-item svg{position:absolute;left:0;top:2px}
.footer-rule{position:absolute;left:100px;top:405px;width:1000px;height:1px;background:#2a2a2a}
.socials{position:absolute;left:496px;top:423px;display:flex;gap:16px}
.socials span{width:40px;height:40px;border-radius:50%;border:1px solid #9a9a9a}
.copyright{position:absolute;left:0;top:510px;width:1200px;text-align:center;font-size:12px;color:#cfcfcf}
</style>
</head>
<body>

<header class="site-header">
  <div class="brand"><span class="dot"></span>tovankreativ.de</div>
  <div class="call">
    <span class="call-icon"><svg width="16" height="16" viewBox="0 0 24 24"><path fill="#1f6cc4" d="M6.6 10.8a15 15 0 0 0 6.6 6.6l2.2-2.2c.3-.3.7-.4 1-.2 1.1.4 2.3.6 3.6.6.6 0 1 .4 1 1V20c0 .6-.4 1-1 1A17 17 0 0 1 3 4c0-.6.4-1 1-1h3.5c.6 0 1 .4 1 1 0 1.3.2 2.5.6 3.6.1.3 0 .7-.2 1z"/></svg></span>
    Call Us : 05600 - 123 456
  </div>
  <nav class="main-nav">
    <span>HOME</span><span>DSGVO</span><span>ABOUT US</span><span>SERVICES</span><span>CREDENTIALS</span><span>CURRENT</span><span>CONTACT</span>
  </nav>
</header>

<section class="hero">
  <div class="hero-photo" role="img" aria-label="Offshore platform lit at night over dark water"></div>
  <h1>WEB DESIGN &amp; Graphic design</h1>
  <div class="hero-arrows">
    <span><svg width="10" height="10" viewBox="0 0 10 10"><path d="M7 1 3 5l4 4" stroke="#fff" stroke-width="2" fill="none"/></svg></span>
    <span><svg width="10" height="10" viewBox="0 0 10 10"><path d="M3 1l4 4-4 4" stroke="#fff" stroke-width="2" fill="none"/></svg></span>
  </div>
  <svg class="hero-curve" width="1200" height="140" viewBox="0 0 1200 140">
    <path d="M0 0 Q 300 150 1200 40 L1200 140 L0 140 Z" fill="#fff"/>
    <path d="M0 0 Q 300 150 1200 40" stroke="#1f6cc4" stroke-width="8" fill="none"/>
  </svg>
</section>

<div class="services-bg"></div>
<h2 class="section-title" style="top:875px">Our Services</h2>
<p class="section-sub" style="top:945px">Sed ut perspiciatis unde omnis iste natus error sit voluptatem accus</p>
<div class="section-rule" style="top:990px"></div>

<div class="services-divider-v"></div>
<div class="services-divider-h"></div>
<div class="center-badge">tovankreativ.de</div>

<article class="service" style="left:195px;top:1095px">
  <svg class="service-icon" viewBox="0 0 60 60"><rect x="6" y="8" width="48" height="34" rx="3" fill="none" stroke="#1d3e6e" stroke-width="3"/><circle cx="30" cy="25" r="8" fill="#1f6cc4"/><rect x="20" y="46" width="20" height="5" fill="#1d3e6e"/></svg>
  <h3>Web Development</h3>
  <p>Sed ut perspiciatis unde omnis iste natus error sit voluptatem accusantium doloremque laudantium, totam rem aperiam, eaque ipsa quae</p>
</article>
<article class="service" style="left:665px;top:1095px">
  <svg class="service-icon" viewBox="0 0 60 60"><rect x="6" y="8" width="48" height="36" fill="none" stroke="#1d3e6e" stroke-width="3"/><rect x="14" y="28" width="6" height="10" fill="#1f6cc4"/><rect x="24" y="20" width="6" height="18" fill="#1f6cc4"/><rect x="34" y="24" width="6" height="14" fill="#1f6cc4"/><path d="M12 44h36" stroke="#1d3e6e" stroke-width="3"/></svg>
  <h3>Marketing</h3>
  <p>Sed ut perspiciatis unde omnis iste natus error sit voluptatem accusantium doloremque laudantium, totam rem aperiam, eaque ipsa quae</p>
</article>
<article class="service" style="left:190px;top:1425px">
  <svg class="service-icon" viewBox="0 0 60 60"><path d="M14 30a10 10 0 0 1 4-19 14 14 0 0 1 26 3 9 9 0 0 1 2 16z" fill="none" stroke="#1d3e6e" stroke-width="3"/><rect x="20" y="34" width="20" height="8" fill="#1f6cc4"/><rect x="20" y="45" width="20" height="8" fill="#1f6cc4"/></svg>
  <h3>Web Hosting</h3>
  <p>Sed ut perspiciatis unde omnis iste natus error sit voluptatem accusantium doloremque laudantium, totam rem aperiam, eaque ipsa quae</p>
</article>
<article class="service" style="left:665px;top:1425px">
  <svg class="service-icon" viewBox="0 0 60 60"><rect x="4" y="10" width="40" height="28" fill="none" stroke="#1d3e6e" stroke-width="3"/><rect x="38" y="20" width="18" height="30" rx="2" fill="#fff" stroke="#1f6cc4" stroke-width="3"/><rect x="14" y="42" width="20" height="4" fill="#1d3e6e"/></svg>
  <h3>Responsive Web Design</h3>
  <p>Sed ut perspiciatis unde omnis iste natus error sit voluptatem accusantium doloremque laudantium, totam rem aperiam, eaque ipsa quae</p>
</article>

<div class="btn-outline" style="left:482px;top:1724px;width:236px;height:54px">VIEW ALL SERVICES</div>

<section class="about">
  <div class="about-photo" role="img" aria-label="Event crowd with a smiling woman in the foreground"></div>
  <svg class="about-panel" width="660" height="500" viewBox="0 0 660 500"><path d="M0 0H562L650 500H0Z" fill="#1f6cc4"/></svg>
  <h2>ABOUT US</h2>
  <div class="lead">Werbeagentur Tovan Kreativ GmbH</div>
  <p class="copy" style="top:163px">The advertising agency TOVAN KREATIV has existed since 1998. Founded under the name TK-Netzdienste, we have been successfully accompanying your projects on the way to the Internet and the big wide advertising world ever since.</p>
  <p class="copy" style="top:280px">The advertising agency TOVAN KREATIV consists of a team of ambitious programmers, designers and marketing experts full of ideas.</p>
  <div class="btn-white">READ MORE</div>
</section>

<div class="clients-bg"></div>
<h2 class="section-title" style="top:2500px">What Clients Say</h2>
<p class="section-sub" style="top:2568px">Sed ut perspiciatis unde omnis iste natus error sit voluptatem accus</p>
<div class="section-rule" style="top:2613px"></div>

<div class="quote-mark" style="left:72px;top:2625px">“</div>
<div class="quote-mark" style="left:920px;top:2790px">”</div>
<div class="slider-arrow" style="left:33px;top:2745px"><svg width="10" height="10" viewBox="0 0 10 10"><path d="M7 1 3 5l4 4" stroke="#333" stroke-width="2" fill="none"/></svg></div>
<div class="slider-arrow" style="left:1126px;top:2745px"><svg width="10" height="10" viewBox="0 0 10 10"><path d="M3 1l4 4-4 4" stroke="#333" stroke-width="2" fill="none"/></svg></div>

<blockquote class="testimonial" style="left:115px;top:2700px;text-align:right">" Sed ut perspiciatis unde omnis iste natus error sit voluptatem accusantium doloremque laudantium, totam rem aperiallo inventore veritatis "<span class="author">- John Doe</span></blockquote>
<div class="avatar" style="left:444px;top:2702px;background:linear-gradient(160deg,#d9c2ad,#8a6a55)" role="img" aria-label="Portrait photo of a client"></div>
<div class="avatar" style="left:624px;top:2702px;background:linear-gradient(160deg,#e3cdb9,#5b3e2e)" role="img" aria-label="Portrait photo of a client"></div>
<blockquote class="testimonial" style="left:785px;top:2700px">" Sed ut perspiciatis unde omnis iste natus error sit voluptatem accusantium doloremque laudantium, totam rem aperiallo inventore veritatis "<span class="author">- John Doe</span></blockquote>

<h2 class="section-title" style="top:3055px">Blog Posts</h2>
<p class="section-sub" style="top:3123px">Sed ut perspiciatis unde omnis iste natus error sit voluptatem accus</p>
<div class="section-rule" style="top:3168px"></div>

<article class="post" style="left:100px;top:3225px">
  <div class="post-image" style="background:linear-gradient(135deg,#1a6aa8,#7fb2d6 50%,#134a78)" role="img" aria-label="Network cables plugged into a switch"></div>
  <h3>Nemo enim ipsam voluptatem</h3>
  <div class="post-meta"><span>02/08/2017</span><span>John Ravi</span></div>
  <p>Nam libero tempore, cum soluta nobis est eligendi optio cumque nihil impedit quo minus</p>
  <div class="btn-outline">Read More ›</div>
</article>
<article class="post" style="left:445px;top:3225px">
  <div class="post-image" style="background:linear-gradient(135deg,#0b1a4a,#2a56b8 50%,#0a1230)" role="img" aria-label="Server racks in a data centre"></div>
  <h3>Nemo enim ipsam voluptatem</h3>
  <div class="post-meta"><span>02/08/2017</span><span>John Ravi</span></div>
  <p>Nam libero tempore, cum soluta nobis est eligendi optio cumque nihil impedit quo minus</p>
  <div class="btn-outline">Read More ›</div>
</article>
<article class="post" style="left:790px;top:3225px">
  <div class="post-image" style="background:linear-gradient(135deg,#cfe0ef,#8fb3d3 50%,#e8eef4)" role="img" aria-label="Man looking at sketches on a glass wall"></div>
  <h3>Nemo enim ipsam voluptatem</h3>
  <div class="post-meta"><span>02/08/2017</span><span>John Ravi</span></div>
  <p>Nam libero tempore, cum soluta nobis est eligendi optio cumque nihil impedit quo minus</p>
  <div class="btn-outline">Read More ›</div>
</article>

<footer class="site-footer">
  <svg class="footer-curve" width="1200" height="180" viewBox="0 0 1200 180">
    <path d="M0 180 L0 150 Q 700 150 1200 0 L1200 180 Z" fill="#050505"/>
    <path d="M0 150 Q 700 150 1200 0" stroke="#1f6cc4" stroke-width="6" fill="none"/>
  </svg>
  <div class="footer-inner"></div>
  <div class="brand"><span class="dot"></span>tovankreativ.de</div>
  <div class="contact-title">CONTACT INFO</div>

  <div class="contact-item" style="left:100px;top:270px">
    <svg width="14" height="16" viewBox="0 0 14 16"><path d="M7 0a6 6 0 0 0-6 6c0 4.5 6 10 6 10s6-5.5 6-10a6 6 0 0 0-6-6zm0 8.5A2.5 2.5 0 1 1 7 3.5a2.5 2.5 0 0 1 0 5z" fill="#ccc"/></svg>
    <strong>TK Netzdienste GmbH &amp; Co. KG</strong><br>Lindenweg 14 | 34100 Felsberg , Germany</div>
  <div class="contact-item" style="left:100px;top:335px">
    <svg width="14" height="16" viewBox="0 0 14 16"><path d="M7 0a6 6 0 0 0-6 6c0 4.5 6 10 6 10s6-5.5 6-10a6 6 0 0 0-6-6zm0 8.5A2.5 2.5 0 1 1 7 3.5a2.5 2.5 0 0 1 0 5z" fill="#ccc"/></svg>
    <strong>Tovan Kreativ GmbH</strong><br>Lindenweg 14 | 34100 Felsberg , Germany</div>

  <div class="contact-item" style="left:425px;top:270px">
    <svg width="14" height="14" viewBox="0 0 24 24"><path fill="#ccc" d="M6.6 10.8a15 15 0 0 0 6.6 6.6l2.2-2.2c.3-.3.7-.4 1-.2 1.1.4 2.3.6 3.6.6.6 0 1 .4 1 1V20c0 .6-.4 1-1 1A17 17 0 0 1 3 4c0-.6.4-1 1-1h3.5c.6 0 1 .4 1 1 0 1.3.2 2.5.6 3.6.1.3 0 .7-.2 1z"/></svg>
    Tel. 05600 - 123 456<br><br>Fax: 05600 - 98 76 54 | Mobile: 0170 - 11 22 333</div>

  <div class="contact-item" style="left:790px;top:270px">
    <svg width="16" height="12" viewBox="0 0 16 12"><path d="M0 0h16v12H0z" fill="#ccc"/><path d="M0 0l8 6 8-6" stroke="#050505" stroke-width="1.5" fill="none"/></svg>
    Jonas Tovan j.tovan@tovankreativ.de<br>Luca Marino l.marino@tovankreativ.de<br>Paul Sander p.sander@tovankreativ.de<br>Accounting buchhaltung@tovankreativ.de</div>

  <div class="footer-rule"></div>
  <div class="socials" aria-label="Social links"><span></span><span></span><span></span><span></span></div>
  <div class="copyright">© copyright 2018 Tovan Kreativ GmbH All Rights Reserved &nbsp;|&nbsp; Privacy policy</div>
</footer>

</body>
</html>
```